KT Crewing business card

Require business card which includes:
Company name: KT CREWING PTY LTD
Email: Mick@ktcrewing.com.au
Phone: 0431 556 208
ACN: 517 238 649

slogan: Onsite Auto Electrician Labour hire

Details and logo on top side
Logo only on bottom side

colour codes : #F15A29 , #939598

Target Market(s)

Western Australia mining sector

Industry/Entity Type

Mining

Contact Information for Business Card

Require business card which includes: Company name: KT CREWING PTY LTD Email: Mick@ktcrewing.com.au Phone: 0431 556 208 ACN: 517 238 649 slogan: Onsite Auto Electrician Labour hire Details and logo on top side Logo only on bottom side colour codes : #F15A29 , #939598

Colors
EE7325
F08F49
F5BC92
FAE3D3
FDF4ED

Requirements
Must have
• double sided

```html
<!DOCTYPE html>
<html lang="en">
<head>
<meta charset="utf-8">
<title>KT Crewing business card</title>
<link href="https://fonts.googleapis.com/css2?family=Poppins:wght@400;500;600;700&display=swap" rel="stylesheet">
<style>
  :root {
    --brand-orange: #F15A29;
    --brand-orange-deep: #E4502A;
    --brand-grey: #939598;
    --card-paper: #EEF1F6;
    --ink: #111111;
    --backdrop: #FFFFFF;
  }
  * { margin: 0; padding: 0; box-sizing: border-box; }
  html, body {
    width: 1200px;
    height: 1122px;
    overflow: hidden;
    background: var(--backdrop);
    font-family: "Poppins", sans-serif;
  }
  .sheet {
    width: 1200px;
    height: 1122px;
    display: flex;
    flex-direction: column;
    align-items: center;
    justify-content: center;
    gap: 46px;
  }
  .card {
    position: relative;
    width: 860px;
    height: 492px;
    box-shadow: 12px 14px 26px rgba(0, 0, 0, 0.28);
    overflow: hidden;
  }

  /* Details side */
  .card--front { background: var(--card-paper); color: var(--ink); }
  .wordmark {
    position: absolute;
    left: 44px;
    top: 30px;
    font-weight: 700;
    font-size: 46px;
    line-height: 1;
    letter-spacing: -0.5px;
    color: var(--brand-orange);
  }
  .company-name {
    position: absolute;
    right: 52px;
    top: 58px;
    font-weight: 600;
    font-size: 35px;
    letter-spacing: 0.3px;
    color: var(--ink);
  }
  .slogan {
    position: absolute;
    left: 40px;
    top: 418px;
    font-size: 17px;
    font-weight: 400;
    color: #1c1c1c;
  }
  .contact-list {
    position: absolute;
    left: 454px;
    top: 355px;
    list-style: none;
    display: grid;
    grid-template-columns: 90px auto;
    row-gap: 12px;
    font-size: 17px;
  }
  .contact-label {
    font-weight: 500;
    display: flex;
    align-items: center;
    gap: 6px;
  }
  .contact-label::before {
    content: "";
    width: 11px;
    height: 11px;
    background: var(--brand-orange);
  }
  .contact-value { font-weight: 400; color: #222; }

  /* Logo side */
  .card--back {
    background: linear-gradient(135deg, var(--brand-orange-deep) 0%, var(--brand-orange) 55%, #EE5526 100%);
  }
  .card--back .texture {
    position: absolute;
    inset: 0;
  }
  .wordmark--reverse {
    position: absolute;
    right: 64px;
    bottom: 56px;
    font-weight: 700;
    font-size: 76px;
    line-height: 1;
    letter-spacing: -1px;
    color: #FFFFFF;
  }
</style>
</head>
<body>
<main class="sheet">
  <section class="card card--front" aria-label="Card details side">
    <div class="wordmark">KT Crewing</div>
    <h1 class="company-name">KT CREWING PTY LTD</h1>
    <p class="slogan">Onsite Auto Electrician Labour hire</p>
    <dl class="contact-list">
      <dt class="contact-label">EMAIL</dt><dd class="contact-value">Mick@ktcrewing.com.au</dd>
      <dt class="contact-label">PHONE</dt><dd class="contact-value">0431 556 208</dd>
      <dt class="contact-label">ACN</dt><dd class="contact-value">517 238 649</dd>
    </dl>
  </section>

  <section class="card card--back" aria-label="Card logo side">
    <svg class="texture" width="860" height="492" role="img" aria-label="Subtle faceted geometric texture in tones of orange">
      <defs>
        <linearGradient id="facet-tone" x1="0" y1="0" x2="1" y2="1">
          <stop offset="0" stop-color="#000" stop-opacity="0.06"/>
          <stop offset="0.5" stop-color="#fff" stop-opacity="0.02"/>
          <stop offset="1" stop-color="#000" stop-opacity="0.04"/>
        </linearGradient>
      </defs>
      <rect width="860" height="492" fill="url(#facet-tone)"/>
    </svg>
    <div class="wordmark--reverse">KT Crewing</div>
  </section>
</main>
</body>
</html>
```